Velvet Fern Beauty Bar Business Card

We need a modern, elegant business card design for our new beauty bar located in La Quinta, CA. The card should feel premium yet approachable, reflecting our brand identity: warm, stylish, and confidence-boosting.

Use our existing Velvet Fern Beauty Bar logo (to be provided as vector file).

Colors: Black, White, Blush / Nude accents, and Gold (metallic or foil effect if possible).

Typography: Clean sans-serif for clarity, with optional elegant script accent.
Design Style

Minimalist and modern with plenty of white space.

Premium look with a beauty/lifestyle feel (not overly corporate).

Option to explore vertical or horizontal orientation.

Rounded corners welcome, but not required.

Additional Notes

Design should print well in both matte and glossy finishes.

Please present mockups with both light and dark backgrounds.

Keep overall feel sleek, feminine, and high-end while still being approachable.

```html
<!DOCTYPE html>
<html lang="en">
<head>
<meta charset="utf-8">
<title>Velvet Fern Beauty Bar – Business Card</title>
<link rel="stylesheet" href="https://fonts.googleapis.com/css2?family=Poppins:wght@300;400;600&display=swap">
<style>
  :root {
    --backdrop-dark: #1b1b1e;
    --backdrop-light: #f3e6e0;
    --card: #232427;
    --ink: #f4f4f4;
    --ink-soft: #c4c5c8;
    --emboss: #3c3d41;
    --gold: #c9a45c;
    --gold-light: #e2c48a;
    --blush: #e8c4b8;
  }
  * { box-sizing: border-box; margin: 0; padding: 0; }
  html, body {
    width: 1200px; height: 800px; overflow: hidden;
    font-family: "Poppins", sans-serif;
    color: var(--ink);
  }
  .stage {
    width: 1200px; height: 800px;
    display: grid; grid-template-columns: 600px 600px;
  }
  .scene {
    display: flex; align-items: center; justify-content: center;
  }
  .scene--dark { background: var(--backdrop-dark); }
  .scene--light { background: var(--backdrop-light); }

  .card {
    position: relative;
    width: 520px; height: 297px;
    background: var(--card);
    border-radius: 22px;
    box-shadow: 0 18px 40px rgba(0,0,0,.45);
    overflow: hidden;
  }
  .scene--light .card { box-shadow: 0 18px 40px rgba(90,60,50,.28); }

  .wordmark {
    position: absolute; left: 0; right: 0;
    display: flex; align-items: center; justify-content: center; gap: 12px;
    font-weight: 400; letter-spacing: 3px;
    text-transform: uppercase; white-space: nowrap;
  }
  .wordmark__dot {
    width: 14px; height: 14px; border-radius: 50%;
    background: var(--gold);
  }
  .byline {
    position: absolute; left: 0; right: 0;
    display: flex; align-items: center; justify-content: center; gap: 12px;
    font-weight: 400; letter-spacing: 2px; white-space: nowrap;
  }
  .byline::before, .byline::after {
    content: ""; width: 34px; height: 1px; background: currentColor;
  }

  /* Front */
  .card--front .wordmark {
    top: 92px; font-size: 32px; color: var(--emboss);
    text-shadow: 0 1px 0 rgba(255,255,255,.07), 0 -1px 0 rgba(0,0,0,.5);
  }
  .card--front .wordmark__dot { background: var(--emboss); }
  .card--front .byline {
    top: 146px; font-size: 15px; color: var(--emboss);
    text-shadow: 0 1px 0 rgba(255,255,255,.06);
  }
  .website {
    position: absolute; left: 0; right: 0; bottom: 46px;
    text-align: center; font-size: 13px; letter-spacing: 7px;
    font-weight: 300; color: var(--gold-light);
  }

  /* Back */
  .card--back .wordmark { top: 34px; font-size: 30px; color: var(--ink); }
  .card--back .byline { top: 84px; font-size: 14px; color: var(--ink); }
  .person {
    position: absolute; left: 0; right: 0; top: 122px; text-align: center;
  }
  .person__name { font-weight: 600; font-size: 19px; letter-spacing: 1.5px; }
  .person__role { font-weight: 300; font-size: 12px; letter-spacing: 1px; color: var(--blush); }
  .divider {
    position: absolute; left: 26px; right: 26px; top: 196px;
    height: 1px; background: var(--gold);
  }
  .contacts {
    position: absolute; left: 28px; bottom: 24px;
    list-style: none; font-size: 13px; font-weight: 300; line-height: 1.9;
  }
  .contacts li { display: flex; align-items: center; gap: 10px; }
  .contacts svg { width: 13px; height: 13px; fill: var(--gold); }
  .address {
    position: absolute; right: 28px; bottom: 28px;
    text-align: right; font-size: 13px; font-weight: 300; line-height: 1.6;
  }
</style>
</head>
<body>
<main class="stage">
  <div class="scene scene--dark">
    <section class="card card--front" aria-label="Card front">
      <div class="wordmark"><span class="wordmark__dot"></span>Velvet Fern</div>
      <p class="byline">Beauty Bar by Lorena</p>
      <p class="website">www.velvetfernbar.com</p>
    </section>
  </div>

  <div class="scene scene--light">
    <section class="card card--back" aria-label="Card back">
      <div class="wordmark"><span class="wordmark__dot"></span>Velvet Fern</div>
      <p class="byline">Beauty Bar by Lorena</p>
      <div class="person">
        <p class="person__name">JORDAN K REYES</p>
        <p class="person__role">CEO</p>
      </div>
      <div class="divider"></div>
      <ul class="contacts">
        <li>
          <svg viewBox="0 0 24 24" aria-hidden="true"><path d="M6.6 10.8a15 15 0 0 0 6.6 6.6l2.2-2.2a1 1 0 0 1 1-.25 11.4 11.4 0 0 0 3.6.57 1 1 0 0 1 1 1V20a1 1 0 0 1-1 1A17 17 0 0 1 3 4a1 1 0 0 1 1-1h3.5a1 1 0 0 1 1 1c0 1.25.2 2.45.57 3.6a1 1 0 0 1-.25 1z"/></svg>
          (555) 014-2290
        </li>
        <li>
          <svg viewBox="0 0 24 24" aria-hidden="true"><path d="M2 5h20v14H2zm2 2v.5l8 5 8-5V7l-8 5z"/></svg>
          hello@velvetfernbar.com
        </li>
      </ul>
      <p class="address">PO Box 48 Palm Lane<br>La Quinta CA</p>
    </section>
  </div>
</main>
</body>
</html>
```